One of a Kind Clean Business Card

We need to design a new business card template for our company. Our company designs and produced merchandising displays. You can see a sample of what we produce on our site www.qorvatfixtures.com. I have uploaded our logo in vector format, as well as a picture of our current business cards. We want a totally different look. We want simple and clean, looking forward to seeing what people create.
Updates

I would like to update the address for Tellur Display Group Inc. 418 N Brindle Ave Fernwood Heights, WI 60817 Would also note. No QR codes

Industry/Entity Type

Business

Contact Information for Business Card

Need a 1 sided business card designed.

Font styles to use
Serif

Requirements
Must have
• Easy to view; Clean Design
Nice to have
• Features that promote engineering and creativity
Should not have
• Too much clutter, keep it simple

```html
<!DOCTYPE html>
<html lang="en">
<head>
<meta charset="utf-8">
<title>Tellur Display Group Inc. — Business Card</title>
<link rel="stylesheet" href="https://fonts.googleapis.com/css2?family=Roboto:wght@400;500&display=swap">
<style>
  :root {
    --backdrop: #d9d5d0;
    --card: #0d0d0d;
    --ink: #ffffff;
    --accent: #8f1d1f;
  }
  * { margin: 0; padding: 0; box-sizing: border-box; }
  html, body {
    width: 1200px; height: 1200px; overflow: hidden;
    background: var(--backdrop);
    font-family: "Roboto", Arial, sans-serif;
  }
  .canvas { position: relative; width: 1200px; height: 1200px; }
  .card {
    position: absolute; left: 214px; width: 772px; height: 438px;
    background: var(--card); color: var(--ink);
    box-shadow: 0 4px 14px rgba(0,0,0,0.25);
  }
  .card--mono { top: 151px; }
  .card--accent { top: 634px; }
  .company-name {
    position: absolute; left: 70px; top: 207px;
    font-size: 23px; font-weight: 400; letter-spacing: 0.2px;
    white-space: nowrap;
  }
  .divider {
    position: absolute; left: 393px; top: 102px;
    width: 2px; height: 235px; background: var(--ink);
  }
  .details { position: absolute; left: 426px; top: 92px; }
  .person-name { font-size: 31px; font-weight: 500; line-height: 36px; }
  .person-role { font-size: 20px; line-height: 24px; }
  .address { margin-top: 17px; font-size: 18px; line-height: 26px; white-space: nowrap; }
  .contact-list { list-style: none; margin-top: 11px; }
  .contact-item {
    display: flex; align-items: center; gap: 6px;
    font-size: 18px; line-height: 27.5px; white-space: nowrap;
  }
  .contact-icon {
    width: 18px; height: 18px; flex: none;
    fill: none; stroke: var(--ink); stroke-width: 1.4;
  }
  .card--accent .company-name,
  .card--accent .person-role { color: var(--accent); }
  .card--accent .divider { background: var(--accent); width: 1.5px; }
  .card--accent .contact-icon { stroke: var(--accent); }
</style>
</head>
<body>
<div class="canvas">

  <section class="card card--mono">
    <div class="company-name">Tellur Display Group Inc.</div>
    <div class="divider"></div>
    <div class="details">
      <h1 class="person-name">RHETT VANCE</h1>
      <p class="person-role">President &amp; CEO</p>
      <p class="address">418 N Brindle<br>Ave Fernwood Heights, WI 60817</p>
      <ul class="contact-list">
        <li class="contact-item"><svg class="contact-icon" viewBox="0 0 18 18"><path d="M4 2l3 3-1.5 2c1 2 3 4 5 5l2-1.5 3 3-2 2C8 15 3 10 2 4z"/></svg>608-555-0142</li>
        <li class="contact-item"><svg class="contact-icon" viewBox="0 0 18 18"><rect x="5" y="1.5" width="8" height="15" rx="1.5"/><path d="M8 14h2"/></svg>414-555-0176</li>
        <li class="contact-item"><svg class="contact-icon" viewBox="0 0 18 18"><rect x="2" y="4" width="14" height="10"/><path d="M2 4l7 6 7-6"/></svg>rvance@qorvatfixtures.com</li>
        <li class="contact-item"><svg class="contact-icon" viewBox="0 0 18 18"><circle cx="9" cy="9" r="7"/><ellipse cx="9" cy="9" rx="3" ry="7"/><path d="M2 9h14M3.5 5h11M3.5 13h11"/></svg>www.qorvatfixtures.com</li>
      </ul>
    </div>
  </section>

  <section class="card card--accent">
    <div class="company-name">Tellur Display Group Inc.</div>
    <div class="divider"></div>
    <div class="details">
      <h2 class="person-name">RHETT VANCE</h2>
      <p class="person-role">President &amp; CEO</p>
      <p class="address">418 N Brindle<br>Ave Fernwood Heights, WI 60817</p>
      <ul class="contact-list">
        <li class="contact-item"><svg class="contact-icon" viewBox="0 0 18 18"><path d="M4 2l3 3-1.5 2c1 2 3 4 5 5l2-1.5 3 3-2 2C8 15 3 10 2 4z"/></svg>608-555-0142</li>
        <li class="contact-item"><svg class="contact-icon" viewBox="0 0 18 18"><rect x="5" y="1.5" width="8" height="15" rx="1.5"/><path d="M8 14h2"/></svg>414-555-0176</li>
        <li class="contact-item"><svg class="contact-icon" viewBox="0 0 18 18"><rect x="2" y="4" width="14" height="10"/><path d="M2 4l7 6 7-6"/></svg>rvance@qorvatfixtures.com</li>
        <li class="contact-item"><svg class="contact-icon" viewBox="0 0 18 18"><circle cx="9" cy="9" r="7"/><ellipse cx="9" cy="9" rx="3" ry="7"/><path d="M2 9h14M3.5 5h11M3.5 13h11"/></svg>www.qorvatfixtures.com</li>
      </ul>
    </div>
  </section>

</div>
</body>
</html>
```